Personal Business Card Design Project

I require a two sided personal business card design.

I am a 35 year old Angel Investor and I invest in various niche internet and F&B projects in China. I am Chinese Australian

One side should be in English and the other side should be in Chinese.

My English details are:

Cole Marsh
Angel Investor

China: +86 1390 274 5183
Hong Kong: +852 6133 4087
Email: cole@cdmarsh.net
Address: Flat 2407, Block 5, Pinecrest Gardens,
42 Maoyuan Road (near Beiling Road),
Shanghai, 200437,
China

My Chinese details are (do not print the text in brackets)

袁哲明 (Name)
天使投资者(Angel Investor)

中国 (China): +86 1390 274 5183
香港 (Hong Kong): +852 6133 4087
Email: cole@cdmarsh.net
地址 (Address): 上海市茂园路42号5号楼2407室
松岭花园, 中国 200437

Target Market(s)

I will only give this card to present to new partners and suppliers and people asking for funding. Not customers.

Industry/Entity Type

Internet

Requirements
Must have
• Something a little humourous in terms of graphics that suggest helping something to grow since I invest in startups. But I want a sophisticated look to it as well.
Nice to have
• Black and White tongue in cheek graphics but not overboard.

The whole card can be not conventional in shape or have cutouts but still retain the business standard business card size.

```html
<!DOCTYPE html>
<html lang="en">
<head>
<meta charset="utf-8">
<title>Cole Marsh — Business Card</title>
<link rel="stylesheet" href="https://fonts.googleapis.com/css2?family=Oswald:wght@600&family=Noto+Sans+SC:wght@300&display=swap">
<style>
  :root {
    --bg-top: #25225f;
    --bg-mid: #8a84ad;
    --bg-bottom: #f4f4f8;
    --card-light: #ffffff;
    --card-dark: #000000;
    --ink-dark: #111111;
    --ink-light: #ffffff;
    --leaf-green: #1f9a48;
    --shadow: rgba(20, 18, 50, 0.55);
  }
  html, body {
    margin: 0;
    padding: 0;
    width: 1200px;
    height: 1033px;
    overflow: hidden;
  }
  body {
    position: relative;
    background: linear-gradient(180deg, var(--bg-top) 0%, var(--bg-mid) 50%, var(--bg-bottom) 100%);
  }
  .card {
    position: absolute;
    left: 243px;
    width: 697px;
    box-shadow: 8px 9px 10px var(--shadow);
    box-sizing: border-box;
  }
  .card--english {
    top: 106px;
    height: 377px;
    background: var(--card-light);
    color: var(--ink-dark);
  }
  .card--chinese {
    top: 548px;
    height: 377px;
    background: var(--card-dark);
    color: var(--ink-light);
  }
  .card__details {
    position: absolute;
    margin: 0;
    padding: 0;
    list-style: none;
    white-space: nowrap;
  }
  .card--english .card__details {
    left: 11px;
    top: 42px;
    font-family: "Oswald", "Arial Narrow", sans-serif;
    font-weight: 600;
    font-size: 21px;
    line-height: 33.5px;
    letter-spacing: 0.2px;
  }
  .card--chinese .card__details {
    left: 21px;
    top: 40px;
    font-family: "Noto Sans SC", "Microsoft YaHei", sans-serif;
    font-weight: 300;
    font-size: 24px;
    line-height: 38px;
  }
  .card__gap { height: 33.5px; }
  .card--chinese .card__gap { height: 38px; }
  .card__emblem {
    position: absolute;
    left: 421px;
    top: 14px;
    width: 230px;
    height: 273px;
    border-radius: 40px 40px 60px 60px;
  }
  .card--english .card__emblem {
    background: linear-gradient(180deg, var(--leaf-green) 0%, var(--leaf-green) 35%, var(--ink-dark) 60%, var(--ink-dark) 100%);
  }
  .card--chinese .card__emblem {
    background: linear-gradient(180deg, var(--leaf-green) 0%, var(--leaf-green) 35%, var(--ink-light) 62%, var(--ink-light) 100%);
  }
</style>
</head>
<body>
  <section class="card card--english">
    <ul class="card__details">
      <li class="card__name">Cole Marsh</li>
      <li class="card__title">Angel Investor</li>
      <li class="card__gap"></li>
      <li>China: +86 1390 274 5183</li>
      <li>Hong Kong: +852 6133 4087</li>
      <li>Email: cole@cdmarsh.net</li>
      <li>Address: Flat 2407, Block 5, Pinecrest Gardens,</li>
      <li>42 Maoyuan Road (near Beiling Road),</li>
      <li>Shanghai, 200437,</li>
      <li>China</li>
    </ul>
    <div class="card__emblem" role="img" aria-label="Card emblem illustration"></div>
  </section>

  <section class="card card--chinese" lang="zh-Hans">
    <ul class="card__details">
      <li class="card__name">袁哲明</li>
      <li class="card__title">天使投资者</li>
      <li class="card__gap"></li>
      <li>中国 : +86 1390 274 5183</li>
      <li>香港 : +852 6133 4087</li>
      <li>Email: cole@cdmarsh.net</li>
      <li>地址 : 上海市茂园路42号5号楼2407室</li>
      <li>松岭花园, 中国 200437</li>
    </ul>
    <div class="card__emblem" role="img" aria-label="Card emblem illustration"></div>
  </section>
</body>
</html>
```